New Company Logo & Responsive Website Design for Codewell Harbor

Codewell Harbor provides a white labeled, digital lending platform technology solutions to the mortgage industry via a SaaS model. Our target market is Mortgage Companies and Banks who are looking for innovative technology to assist both borrowers and loan originators with the lending process, while automating as much of he process as possible.

Codewell Harbor is our company name, and our modular software offerings Include the following Products:

1) Applicant Harbor: A customizable, web based, point-of-sale application for borrowers to complete a loan application, and guide them through the mortgage process.

POS Definition
"A point of sale (POS) is the client-facing software solution that allows borrowers to create a customer portal, apply for a loan online, and seamlessly submit needed documentation."

2) Lending Harbor: A Mortgage Loan Origination System

LOS Definition
"A Mortgage Loan Origination System (LOS) is a platform that takes a completed loan application and facilitates the mortgage transaction from origination to post closing. LOS systems may include document management, pricing and eligibility engines, and compliance tools to decrease risk and increase loan manufacturing quality.

3) Dwelling Harbor: A brandable, home search website

The LOS and POS definitions provided above are just for your understanding of what these products are, not to be included word-for-word as website content.

We are looking for designs that are elegant, convey technical competency, simple to navigate, and set us apart from the competition.

We are not set on any particular colors at this point, so feel free to choose the best colors for your particular designs.

Please include company logo, both desktop and mobile designs with a template design for the website sub pages.

Some Examples of Mortgage Technology Websites offering similar products. These are to show the typical content, not designs that we particularly like or dislike.

https://quentrapo.com/
https://www.brivatokel.com/
https://www.dwarnomivex.com/
https://www.trelpanosky.com/
https://www.vondriquel.com/products/trail

Please send comments with additional questions.

Thank You For your participation.

Target Market(s)

Mortgage Companies

Number of Pages Required

2 page

```html
<!DOCTYPE html>
<html lang="en">
<head>
<meta charset="utf-8">
<title>Codewell Harbor — Digital Lending Platform</title>
<link href="https://fonts.googleapis.com/css2?family=Roboto:wght@400;500;700&display=swap" rel="stylesheet">
<style>
:root{
  --green:#3f7d12;
  --green-dark:#2f6a06;
  --green-light:#6fae2a;
  --tint:#f1f7ec;
  --ink:#111;
  --muted:#666;
  --line:#bdbdbd;
  --footer:#0d190a;
  --star:#f39c12;
}
*{box-sizing:border-box;margin:0;padding:0}
html,body{width:1200px;height:4910px;overflow:hidden}
body{font-family:'Roboto',Arial,sans-serif;color:var(--ink);background:#fff;position:relative}
.abs{position:absolute}
.accent{color:var(--green)}
.art{position:absolute;border-radius:14px}

/* header */
.hero-band{position:absolute;left:0;top:0;width:1200px;height:600px}
.brand{left:112px;top:46px;font-size:29px;font-weight:500}
.nav{left:454px;top:54px;display:flex;font-size:15px;font-weight:500;color:#fff}
.nav a{color:#fff;text-decoration:none;margin-right:30px}
.nav a.home{color:var(--ink)}
.btn-account{left:934px;top:45px;width:154px;height:40px;border-radius:20px;background:#fff;color:var(--ink);font-size:15px;font-weight:500;display:flex;align-items:center;justify-content:center}

.hero-art{left:610px;top:130px;width:545px;height:450px;background:linear-gradient(160deg,#c6d9ec 0%,#e9eef3 55%,#f6e3c9 100%)}
.hero-title{left:112px;top:212px;width:460px;font-size:38px;line-height:47px;font-weight:500;z-index:1}
.hero-title b{color:var(--green);font-weight:500}
.hero-text{left:112px;top:422px;width:480px;font-size:12.5px;line-height:22px;color:var(--muted);z-index:1}
.btn{display:flex;align-items:center;justify-content:center;background:var(--green-dark);color:#fff;font-weight:500;border-radius:22px}
.btn-start{left:112px;top:515px;width:134px;height:40px;font-size:15px}

.section-title{position:absolute;left:0;width:1200px;text-align:center;font-size:32px;font-weight:500}

/* offerings */
.card{position:absolute;top:800px;width:258px;height:288px;background:#fff;border-radius:8px;box-shadow:0 2px 10px rgba(0,0,0,.09)}
.card .art{left:30px;top:22px;width:198px;height:180px;background:radial-gradient(circle at 50% 45%,#e8f3dc 0,#c7d9ee 55%,#fff 80%)}
.card .label{position:absolute;left:0;bottom:38px;width:100%;text-align:center;font-size:18px;font-weight:500}

/* how it works */
.how{position:absolute;left:6px;top:1204px;width:1194px;height:1878px;background:var(--tint)}
.step-title{position:absolute;font-size:28px;font-weight:500}
.step-text{position:absolute;width:370px;font-size:12.5px;line-height:22.5px;color:var(--muted)}
.step-text p+p{margin-top:22px}

/* testimonials */
.review{position:absolute;top:3282px;width:285px}
.stars{display:flex;gap:3px;margin-bottom:24px}
.review .quote{font-size:12.5px;line-height:22.5px;color:#555}
.review .name{margin-top:28px;font-size:12.5px;font-weight:500}
.dots{position:absolute;left:565px;top:3555px;display:flex;gap:5px}
.dots i{width:10px;height:10px;border-radius:50%;background:#d6d6d6}
.dots i.on{background:#9a9a9a}

/* contact */
.contact{position:absolute;left:0;top:3680px;width:1200px;height:772px;background:var(--tint)}
.field{position:absolute;left:128px;width:451px;height:70px;border-bottom:1px solid var(--line);font-size:12.5px;color:#555}
.btn-submit{left:444px;top:4303px;width:135px;height:40px;font-size:15px}

/* footer */
.footer{position:absolute;left:0;top:4452px;width:1200px;height:458px;background:var(--footer);color:#fff}
.f-brand{left:133px;top:110px;font-size:26px;font-weight:500}
.f-text{left:133px;top:166px;width:300px;font-size:12.5px;line-height:22.5px}
.f-follow{left:133px;top:285px;font-size:15px;font-weight:500;display:flex;align-items:center;gap:10px}
.f-follow span.soc{width:24px;height:24px;border-radius:50%;background:#fff;display:inline-block}
.f-head{top:104px;font-size:24px;font-weight:500;letter-spacing:.5px}
.f-item{font-size:14px;display:flex;align-items:center;gap:14px;line-height:26px}
.copy{left:0;top:398px;width:1200px;text-align:center;font-size:12px}
</style>
</head>
<body>

<!-- Header / hero -->
<svg class="hero-band" viewBox="0 0 1200 600" aria-hidden="true">
  <defs><linearGradient id="gband" x1="0" y1="0" x2="1" y2="1"><stop offset="0" stop-color="#5d9e1c"/><stop offset="1" stop-color="#2f6a06"/></linearGradient></defs>
  <polygon points="472,0 1200,0 1200,70 655,185" fill="url(#gband)"/>
</svg>
<div class="art hero-art" role="img" aria-label="Illustration of a person placing a coin on the roof of a house with a ladder and coin stacks"></div>
<div class="abs brand">Codewell <span class="accent">Harbor</span>.</div>
<nav class="abs nav"><a class="home">Home</a><a>About Us</a><a>Services</a><a>How it works</a><a>Contact Us</a></nav>
<div class="abs btn-account">Create Account</div>

<h1 class="abs hero-title">Digital lending platform technology solutions to the <b>mortgage industry via a SaaS model</b>.</h1>
<p class="abs hero-text">Lorem ipsum dolor sit amet, consectetur adipiscing elit, sed do eiusmod tempor incididunt ut labore et dolore magna aliqua. Quis ipsum suspendisse ultrices gravida. Risus commodo viverra maecenas</p>
<div class="abs btn btn-start">Get Started</div>

<!-- Offerings -->
<h2 class="section-title" style="top:700px">Our Modular <span class="accent">Software Offerings</span>.</h2>
<div class="card" style="left:187px"><div class="art" role="img" aria-label="Illustration of a family beside a house with tree and coins"></div><div class="label">Applicant Harbor</div></div>
<div class="card" style="left:471px"><div class="art" role="img" aria-label="Illustration of a house on a tablet with coins and percent sign"></div><div class="label">Lending Harbor</div></div>
<div class="card" style="left:756px"><div class="art" role="img" aria-label="Illustration of a house with a key and coin"></div><div class="label">Dwelling Harbor</div></div>

<!-- How it works -->
<section class="how"></section>
<h2 class="section-title" style="top:1300px">How It <span class="accent">Works</span>.</h2>

<h3 class="step-title" style="left:193px;top:1438px">Create a customer portal</h3>
<div class="step-text" style="left:195px;top:1495px"><p>Lorem ipsum dolor sit amet, consectetur adipiscing elit, sed do eiusmod tempor incididunt ut labore et dolore magna aliqua. Quis ipsum suspendisse ultrices gravida. Risus commodo viverra maecenas accumsan lacus vel facilisis.</p><p>Lorem ipsum dolor sit amet, consectetur adipiscing elit, sed do eiusmod tempor incididunt ut labore et dolore magna aliqua. Quis ipsum suspendisse ultrices gravida. Risus commodo viverra maecenas accumsan lacus vel facilisis.</p></div>
<div class="art" role="img" aria-label="Illustration of people building an online portal on a tablet and phone" style="left:629px;top:1372px;width:381px;height:304px;background:linear-gradient(150deg,#bfeef3,#e7f1ea 60%,#f6d6dc)"></div>

<div class="art" role="img" aria-label="Illustration of a person checking an online application form with hourglass and books" style="left:181px;top:1810px;width:391px;height:285px;background:linear-gradient(150deg,#f8d6cc,#e5f3ef 50%,#bfeaf0)"></div>
<h3 class="step-title" style="left:648px;top:1824px">Apply for a loan online</h3>
<div class="step-text" style="left:649px;top:1880px"><p>Lorem ipsum dolor sit amet, consectetur adipiscing elit, sed do eiusmod tempor incididunt ut labore et dolore magna aliqua. Quis ipsum suspendisse ultrices gravida. Risus commodo viverra maecenas accumsan lacus vel facilisis.</p><p>Lorem ipsum dolor sit amet, consectetur adipiscing elit, sed do eiusmod tempor incididunt ut labore et dolore magna aliqua. Quis ipsum suspendisse ultrices gravida. Risus commodo viverra maecenas accumsan lacus vel facilisis.</p></div>

<h3 class="step-title" style="left:187px;top:2244px">Submit needed documentation</h3>
<div class="step-text" style="left:189px;top:2300px"><p>Lorem ipsum dolor sit amet, consectetur adipiscing elit, sed do eiusmod tempor incididunt ut labore et dolore magna aliqua. Quis ipsum suspendisse ultrices gravida. Risus commodo viverra maecenas accumsan lacus vel facilisis.</p><p>Lorem ipsum dolor sit amet, consectetur adipiscing elit, sed do eiusmod tempor incididunt ut labore et dolore magna aliqua. Quis ipsum suspendisse ultrices gravida. Risus commodo viverra maecenas accumsan lacus vel facilisis.</p></div>
<div class="art" role="img" aria-label="Illustration of people sending documents from a large laptop" style="left:648px;top:2191px;width:371px;height:352px;background:linear-gradient(150deg,#c7eef6,#eef3f1 60%,#dfe7e3)"></div>

<div class="art" role="img" aria-label="Illustration of an approved loan clipboard with a person holding a tablet" style="left:210px;top:2638px;width:314px;height:305px;background:linear-gradient(150deg,#bfe9ee,#eef2ea 55%,#f7e2b5)"></div>
<h3 class="step-title" style="left:611px;top:2651px">Get your loan</h3>
<div class="step-text" style="left:613px;top:2706px"><p>Lorem ipsum dolor sit amet, consectetur adipiscing elit, sed do eiusmod tempor incididunt ut labore et dolore magna aliqua. Quis ipsum suspendisse ultrices gravida. Risus commodo viverra maecenas accumsan lacus vel facilisis.</p><p>Lorem ipsum dolor sit amet, consectetur adipiscing elit, sed do eiusmod tempor incididunt ut labore et dolore magna aliqua. Quis ipsum suspendisse ultrices gravida. Risus commodo viverra maecenas accumsan lacus vel facilisis.</p></div>

<!-- Testimonials -->
<h2 class="section-title" style="top:3184px">Our Happy <span class="accent">Customers</span>.</h2>
<svg width="0" height="0" style="position:absolute"><defs>
  <symbol id="star" viewBox="0 0 20 20"><polygon points="10,1 12.6,7 19,7.4 14,11.6 15.6,18 10,14.5 4.4,18 6,11.6 1,7.4 7.4,7" fill="var(--star)"/></symbol>
  <symbol id="star-o" viewBox="0 0 20 20"><polygon points="10,2.2 12.3,7.6 18,8 13.6,11.7 15,17.4 10,14.3 5,17.4 6.4,11.7 2,8 7.7,7.6" fill="none" stroke="var(--star)" stroke-width="1.6"/></symbol>
</defs></svg>
<div class="review" style="left:133px">
  <div class="stars"><svg width="18" height="18"><use href="#star"/></svg><svg width="18" height="18"><use href="#star"/></svg><svg width="18" height="18"><use href="#star"/></svg><svg width="18" height="18"><use href="#star"/></svg><svg width="18" height="18"><use href="#star-o"/></svg></div>
  <p class="quote">The standard chunk of Lorem Ipsum used since the 1500s is reproduced below for those interested. Sections 1.10.32 and 1.10.33 from "de Finibus Bonorum et Malorum" by Cicero are also reproduced</p>
  <p class="name">Customer Name</p>
</div>
<div class="review" style="left:457px">
  <div class="stars"><svg width="18" height="18"><use href="#star"/></svg><svg width="18" height="18"><use href="#star"/></svg><svg width="18" height="18"><use href="#star"/></svg><svg width="18" height="18"><use href="#star"/></svg><svg width="18" height="18"><use href="#star-o"/></svg></div>
  <p class="quote">The standard chunk of Lorem Ipsum used since the 1500s is reproduced below for those interested. Sections 1.10.32 and 1.10.33 from "de Finibus Bonorum et Malorum" by Cicero are also reproduced</p>
  <p class="name">Customer Name</p>
</div>
<div class="review" style="left:781px">
  <div class="stars"><svg width="18" height="18"><use href="#star"/></svg><svg width="18" height="18"><use href="#star"/></svg><svg width="18" height="18"><use href="#star"/></svg><svg width="18" height="18"><use href="#star"/></svg><svg width="18" height="18"><use href="#star-o"/></svg></div>
  <p class="quote">The standard chunk of Lorem Ipsum used since the 1500s is reproduced below for those interested. Sections 1.10.32 and 1.10.33 from "de Finibus Bonorum et Malorum" by Cicero are also reproduced</p>
  <p class="name">Customer Name</p>
</div>
<div class="dots"><i></i><i></i><i class="on"></i><i></i><i></i></div>

<!-- Contact -->
<section class="contact"></section>
<h2 class="section-title" style="top:3777px">Get In <span class="accent">Touch With Us</span>.</h2>
<div class="field" style="top:3934px">First Name</div>
<div class="field" style="top:4004px">Last Name</div>
<div class="field" style="top:4075px">Phone Number</div>
<div class="field" style="top:4145px">Email Address</div>
<div class="field" style="top:4216px">Your message goes here</div>
<div class="abs btn btn-submit">Submit Now</div>
<div class="art" role="img" aria-label="Illustration of a support agent at a desk beside a large phone showing contacts and a potted plant" style="left:667px;top:3867px;width:409px;height:438px;background:linear-gradient(150deg,#cfe0fa,#eef3f6 55%,#c9f0e4)"></div>

<!-- Footer -->
<footer class="footer">
  <div class="abs f-brand">Codewell Harbor.</div>
  <p class="abs f-text">Lorem ipsum dolor sit amet, consectetur adipiscing elit, sed do eiusmod tempor incididunt ut labore et dolore magna aliqua. Quis ipsum suspendisse ultrices gravida.</p>
  <div class="abs f-follow">Follow Us :&nbsp;<span class="soc"></span><span class="soc"></span><span class="soc"></span><span class="soc"></span></div>

  <div class="abs f-head" style="left:503px">CONTACT US</div>
  <div class="abs f-item" style="left:512px;top:166px"><svg width="18" height="18" viewBox="0 0 24 24"><path d="M6.6 10.8a15 15 0 0 0 6.6 6.6l2.2-2.2a1 1 0 0 1 1-.25 11.4 11.4 0 0 0 3.6.57 1 1 0 0 1 1 1V20a1 1 0 0 1-1 1A17 17 0 0 1 3 4a1 1 0 0 1 1-1h3.5a1 1 0 0 1 1 1c0 1.25.2 2.45.57 3.57a1 1 0 0 1-.25 1z" fill="#fff"/></svg>415 555 0148</div>
  <div class="abs f-item" style="left:512px;top:217px"><svg width="18" height="16" viewBox="0 0 24 18"><path d="M1 1h22v16H1z" fill="#fff"/><path d="M1 1l11 8 11-8" fill="none" stroke="#0d190a" stroke-width="2"/></svg>info@codewellharbor.com</div>
  <div class="abs f-item" style="left:512px;top:268px;align-items:flex-start"><svg width="16" height="22" viewBox="0 0 16 22"><path d="M8 0a8 8 0 0 1 8 8c0 6-8 14-8 14S0 14 0 8a8 8 0 0 1 8-8z" fill="#fff"/><circle cx="8" cy="8" r="3" fill="#0d190a"/></svg><span>123 Street Name, Location Name,<br>234-567</span></div>

  <div class="abs f-head" style="left:901px">QUICK LINKS</div>
  <div class="abs" style="left:901px;top:166px">
    <div class="f-item" style="gap:10px;line-height:31px"><svg width="16" height="16" viewBox="0 0 16 16"><circle cx="8" cy="8" r="8" fill="#fff"/><path d="M6.5 4.5 10 8l-3.5 3.5" fill="none" stroke="#0d190a" stroke-width="2"/></svg>Home</div>
    <div class="f-item" style="gap:10px;line-height:31px"><svg width="16" height="16" viewBox="0 0 16 16"><circle cx="8" cy="8" r="8" fill="#fff"/><path d="M6.5 4.5 10 8l-3.5 3.5" fill="none" stroke="#0d190a" stroke-width="2"/></svg>About Us</div>
    <div class="f-item" style="gap:10px;line-height:31px"><svg width="16" height="16" viewBox="0 0 16 16"><circle cx="8" cy="8" r="8" fill="#fff"/><path d="M6.5 4.5 10 8l-3.5 3.5" fill="none" stroke="#0d190a" stroke-width="2"/></svg>Our Services</div>
    <div class="f-item" style="gap:10px;line-height:31px"><svg width="16" height="16" viewBox="0 0 16 16"><circle cx="8" cy="8" r="8" fill="#fff"/><path d="M6.5 4.5 10 8l-3.5 3.5" fill="none" stroke="#0d190a" stroke-width="2"/></svg>How It Works</div>
    <div class="f-item" style="gap:10px;line-height:31px"><svg width="16" height="16" viewBox="0 0 16 16"><circle cx="8" cy="8" r="8" fill="#fff"/><path d="M6.5 4.5 10 8l-3.5 3.5" fill="none" stroke="#0d190a" stroke-width="2"/></svg>Contact Us</div>
  </div>

  <div class="abs copy">Copyright 2022 © Codewell Harbor.com | All Rights Reserved.</div>
</footer>

</body>
</html>
```